Corvelle Strategies business card

I need a business card for my new strategic consulting LLC, Corvelle Strategies. We specialize in helping people who care about broadband technology and telecommunications policy, and we're based in Washington DC. I'm looking for a card that says smart, credible, future-facing and signals a high level of expertise. It's DC, so there's clearly a limit to how crazy we can go with this card, but I am looking for a design that reflects a company that is comfortable with technology, policy, and having a little bit fun. I'm uploading my logo below, and I'd like to have it be part of the card design in some fashion.
Target Market(s)
Telecommunications and technology policy professionals
Industry/Entity Type
Technology policy
Contact Information for Business Card
Name of business, my name (Glen Mosswater), email (glen@corvellestrategies-example.com) , phone number (202-555-0148)phone number

```html
<!DOCTYPE html>
<html lang="en">
<head>
<meta charset="utf-8">
<title>Corvelle Strategies — Business Card</title>
<link rel="stylesheet" href="https://fonts.googleapis.com/css2?family=Domine:wght@700&family=Montserrat:wght@400&display=swap">
<style>
  :root {
    --backdrop: #8e8e8e;
    --paper: #ffffff;
    --ink: #2b2b2b;
    --brand-blue: #0054a0;
    --brand-gold: #f9ae3f;
    --card-dark: #1e1e1e;
    --silver: #c4c4c4;
  }
  * { margin: 0; padding: 0; box-sizing: border-box; }
  html, body {
    width: 1200px; height: 1000px; overflow: hidden;
    background: var(--backdrop);
  }
  .card {
    position: absolute;
    left: 286px;
    width: 628px;
    height: 359px;
    border-radius: 23px;
    overflow: hidden;
  }
  .card--front { top: 103px; background: var(--paper); }
  .card--back { top: 538px; background: var(--card-dark); }

  .wordmark {
    position: absolute;
    display: flex;
    align-items: center;
    gap: 10px;
    font-family: "Domine", Georgia, serif;
    font-weight: 700;
    white-space: nowrap;
  }
  .wordmark__dot {
    border-radius: 50%;
    background: var(--brand-gold);
    flex: none;
  }
  .card--front .wordmark {
    left: 52px; top: 66px;
    font-size: 34px;
    color: var(--brand-blue);
  }
  .card--front .wordmark__dot { width: 20px; height: 20px; }

  .contact-list {
    position: absolute;
    left: 52px; top: 198px;
    list-style: none;
    font-family: "Montserrat", Arial, sans-serif;
    font-size: 13.5px;
    color: var(--ink);
    letter-spacing: 0.2px;
    white-space: nowrap;
  }
  .contact-list li {
    display: flex; align-items: center;
    height: 22px;
  }
  .contact-list svg {
    width: 12px; height: 12px;
    margin-right: 9px;
    fill: var(--brand-blue);
    flex: none;
  }
  .holder-name {
    position: absolute;
    right: 44px; top: 225px;
    font-family: "Domine", Georgia, serif;
    font-weight: 700;
    font-size: 25px;
    color: var(--brand-blue);
    letter-spacing: 0.3px;
    white-space: nowrap;
  }
  .accent-band {
    position: absolute;
    left: 0; bottom: 0;
    width: 100%; height: 19px;
  }

  .card--back .wordmark {
    left: 50%; top: 50%;
    transform: translate(-50%, -50%);
    font-size: 46px;
    color: var(--silver);
    gap: 14px;
  }
  .card--back .wordmark__dot { width: 28px; height: 28px; }
</style>
</head>
<body>
  <section class="card card--front" aria-label="Card front">
    <div class="wordmark">Corvelle Strategies<span class="wordmark__dot"></span></div>

    <ul class="contact-list">
      <li>
        <svg viewBox="0 0 24 24" aria-hidden="true"><path d="M12 1a8 8 0 0 0-8 8c0 6 8 14 8 14s8-8 8-14a8 8 0 0 0-8-8zm0 11a3 3 0 1 1 0-6 3 3 0 0 1 0 6z"/></svg>
        Washington DC
      </li>
      <li>
        <svg viewBox="0 0 24 24" aria-hidden="true"><path d="M6.6 10.8a15 15 0 0 0 6.6 6.6l2.2-2.2a1 1 0 0 1 1-.25 11.4 11.4 0 0 0 3.6.57 1 1 0 0 1 1 1V20a1 1 0 0 1-1 1A17 17 0 0 1 3 4a1 1 0 0 1 1-1h3.5a1 1 0 0 1 1 1c0 1.250.2 2.450.57 3.57a1 1 0 0 1-.25 1z"/></svg>
        202-555-0148
      </li>
      <li>
        <svg viewBox="0 0 24 24" aria-hidden="true"><path d="M2 4h20v16H2zm2 2v.5l8 5.5 8-5.5V6zm0 3v9h16V9l-8 5.5z"/></svg>
        glen@corvellestrategies-example.com
      </li>
      <li>
        <svg viewBox="0 0 24 24" aria-hidden="true"><path d="M12 2a10 10 0 1 0 0 20 10 10 0 0 0 0-20zm-1 17.9A8 8 0 0 1 4 12l5 5v1a2 2 0 0 0 2 2zm6.9-2.5A2 2 0 0 0 16 16h-1v-3a1 1 0 0 0-1-1H8v-2h2a1 1 0 0 0 1-1V7h2a2 2 0 0 0 2-2v-.4a8 8 0 0 1 2.9 12.8z"/></svg>
        corvellestrategies-example.com
      </li>
    </ul>

    <div class="holder-name">Glen Mosswater</div>

    <svg class="accent-band" viewBox="0 0 628 19" preserveAspectRatio="none" aria-hidden="true">
      <rect x="0" y="0" width="628" height="19" fill="var(--brand-gold)"/>
      <path d="M0 0H500C470 6 470 13 500 19H0Z" fill="var(--brand-blue)"/>
      <path d="M500 0C470 6 470 13 500 19H515C485 13 485 6 515 0Z" fill="var(--paper)"/>
    </svg>
  </section>

  <section class="card card--back" aria-label="Card back">
    <div class="wordmark">Corvelle Strategies<span class="wordmark__dot"></span></div>
  </section>
</body>
</html>
```